Business card/ Letterhead/ Envelope Design for Dental Office
Brent Vasko
Business card/ Letterhead/ Envelope Design for Dental Office  - Health
Creative Brief
Professional
4275 Larkspur Ln Ste 200
vaskodds@pinehollowdental.example
vaskodds vaskodds
if you can update all the ones with ratings that'd be great to see updates. 1) change name to read Brent K. Vasko D.D.S. 2) under name if you can add General Dentist 3) will need full address: 4275 Larkspur Ln Ste 200 Sun Prairie, WI 53590 4) include fax number (608) 555-0147

```html
<!DOCTYPE html>
<html lang="en">
<head>
<meta charset="utf-8">
<title>Pine Hollow Dental Center – Business Card</title>
<link rel="stylesheet" href="https://fonts.googleapis.com/css2?family=Questrial&display=swap">
<style>
  :root {
    --navy: #1e3f7a;
    --sky: #3b97dd;
    --sky-light: #7cc0ef;
    --paper: #ffffff;
    --backdrop: #e6e4e0;
  }
  * { margin: 0; padding: 0; box-sizing: border-box; }
  html, body { width: 1200px; height: 904px; overflow: hidden; }
  body {
    background: var(--backdrop);
    font-family: "Questrial", "Century Gothic", sans-serif;
    position: relative;
  }
  .card {
    position: absolute;
    width: 700px;
    height: 400px;
    left: 250px;
    overflow: hidden;
    box-shadow: 0 6px 18px rgba(0,0,0,0.18);
  }
  .card--front { top: 40px; background: var(--navy); }
  .card--back { top: 464px; background: var(--paper); }

  .brand { position: absolute; display: flex; align-items: center; gap: 14px; white-space: nowrap; }
  .brand__dot { width: 50px; height: 50px; border-radius: 50%; background: var(--sky); flex: none; }
  .brand__name { font-size: 28px; line-height: 1; letter-spacing: 0.5px; }
  .card--front .brand { left: 50%; top: 50%; transform: translate(-50%, -50%); }
  .card--front .brand__name { color: var(--paper); }
  .card--back .brand { left: 48px; top: 72px; }
  .card--back .brand__name { color: var(--navy); }

  .back__band {
    position: absolute; left: 0; right: 0; bottom: 0; height: 212px;
    background: var(--navy);
  }
  .back__accent { position: absolute; right: -110px; top: 30px; width: 320px; height: 320px; }

  .contact { position: absolute; left: 48px; bottom: 22px; color: var(--paper); }
  .contact__name { color: var(--sky-light); font-size: 19px; line-height: 1; }
  .contact__title { color: var(--paper); font-size: 13px; line-height: 1; margin: 6px 0 12px; letter-spacing: 0.5px; }
  .contact__row { display: flex; align-items: center; gap: 10px; font-size: 14px; line-height: 1; margin-bottom: 8px; }
  .contact__row:last-child { margin-bottom: 0; }
  .contact__icon { width: 13px; height: 13px; flex: none; }
</style>
</head>
<body>

<section class="card card--front" aria-label="Card front">
  <div class="brand">
    <span class="brand__dot"></span>
    <span class="brand__name">Pine Hollow Dental Center</span>
  </div>
</section>

<section class="card card--back" aria-label="Card back">
  <div class="brand">
    <span class="brand__dot"></span>
    <span class="brand__name">Pine Hollow Dental Center</span>
  </div>

  <div class="back__band"></div>

  <svg class="back__accent" viewBox="0 0 320 320" aria-hidden="true">
    <circle cx="160" cy="160" r="156" fill="var(--paper)"/>
    <circle cx="160" cy="160" r="142" fill="var(--sky)"/>
  </svg>

  <div class="contact">
    <p class="contact__name">Brent K. Vasko D.D.S.</p>
    <p class="contact__title">General Dentist</p>
    <p class="contact__row">
      <svg class="contact__icon" viewBox="0 0 16 16" aria-hidden="true"><path d="M8 1a5 5 0 0 0-5 5c0 4 5 9 5 9s5-5 5-9a5 5 0 0 0-5-5zm0 7a2 2 0 1 1 0-4 2 2 0 0 1 0 4z" fill="var(--sky-light)"/></svg>
      4275 Larkspur Ln Ste 200 Sun Prairie, WI 53590
    </p>
    <p class="contact__row">
      <svg class="contact__icon" viewBox="0 0 16 16" aria-hidden="true"><path d="M4 1l3 3-2 2c1 2 3 4 5 5l2-2 3 3-2 3C7 15 1 9 1 3z" fill="var(--sky-light)"/></svg>
      608-555-0182
    </p>
    <p class="contact__row">
      <svg class="contact__icon" viewBox="0 0 16 16" aria-hidden="true"><rect x="2" y="6" width="12" height="7" rx="1" fill="var(--sky-light)"/><rect x="4" y="2" width="8" height="4" fill="none" stroke="var(--sky-light)" stroke-width="1.2"/></svg>
      Fax (608) 555-0147
    </p>
    <p class="contact__row">
      <svg class="contact__icon" viewBox="0 0 16 16" aria-hidden="true"><circle cx="8" cy="8" r="7" fill="var(--sky-light)"/><path d="M4 5.5h8v5H4z M4 5.5l4 3 4-3" fill="none" stroke="var(--navy)" stroke-width="1"/></svg>
      vaskodds@pinehollowdental.example
    </p>
  </div>
</section>

</body>
</html>
```